Songs Cover Art. Song tittle DJ K - Turn the Lights Low

Hey

I need a cover art for my songs. My genre is Big Room House/EDM music and my DJ name is DJ K. Song title is Turn the Lights Low. I'm a producer and i need a designer to design all my cover art so that i will be able upload my song with a cover art. Do let me know if you have any questions.

Song Tittle: Turn the Lights Low
Artist name: DJ K

Thanks

Reason: I will give more time in order for you guys to create more design!

Industry/Entity Type

House

Requirements
Should not have
• Please dont make the design to colourful.

```html
<!DOCTYPE html>
<html lang="en">
<head>
<meta charset="utf-8">
<title>DJ K - Turn the Lights Low</title>
<link rel="stylesheet" href="https://fonts.googleapis.com/css2?family=Archivo:wdth,wght@125,700;125,900&family=PT+Sans&display=swap">
<style>
  :root {
    --page-bg: #f7fde0;
    --sheet-bg: #ffffff;
    --sheet-edge: #c9ccbc;
    --sheet-shadow: #9a9e86;
    --label-ink: #1a1a1a;
    --cover-bg: #231f20;
    --cover-title: #ffffff;
    --cover-tag: #f2e700;
  }
  html, body {
    margin: 0;
    padding: 0;
    width: 1200px;
    height: 901px;
    overflow: hidden;
    background: var(--page-bg);
  }
  .presentation-sheet {
    position: absolute;
    left: 18px;
    top: 18px;
    width: 1154px;
    height: 847px;
    background: var(--sheet-bg);
    border: 1px solid var(--sheet-edge);
    box-shadow: 9px 9px 0 var(--sheet-shadow);
    box-sizing: border-box;
  }
  .sheet-label {
    position: absolute;
    left: 31px;
    top: 20px;
    margin: 0;
    font-family: "PT Sans", sans-serif;
    font-weight: 400;
    font-size: 18px;
    color: var(--label-ink);
    text-decoration: underline;
    text-underline-offset: 3px;
  }
  .cover-art {
    position: absolute;
    left: 316px;
    top: 157px;
    width: 524px;
    height: 524px;
    display: block;
  }
  .cover-art .cover-bg { fill: var(--cover-bg); }
  .cover-art .song-title {
    font-family: "Archivo", sans-serif;
    font-stretch: 125%;
    font-weight: 900;
    fill: var(--cover-title);
  }
  .cover-art .artist-tag {
    font-family: "Archivo", sans-serif;
    font-stretch: 125%;
    font-weight: 700;
    font-size: 12px;
    fill: var(--cover-tag);
    text-anchor: middle;
  }
</style>
</head>
<body>
  <main class="presentation-sheet">
    <h1 class="sheet-label">DJ K - Turn the Lights Low</h1>

    <svg class="cover-art" viewBox="0 0 524 524" xmlns="http://www.w3.org/2000/svg" aria-label="Cover art: DJ K - Turn the Lights Low">
      <rect class="cover-bg" x="0" y="0" width="524" height="524"/>

      <g class="artist-tag-rows">
        <g class="artist-tag-row" transform="translate(0 20)">
          <text class="artist-tag" x="27">DJ K</text><text class="artist-tag" x="93">DJ K</text><text class="artist-tag" x="159">DJ K</text><text class="artist-tag" x="225">DJ K</text><text class="artist-tag" x="291">DJ K</text><text class="artist-tag" x="357">DJ K</text><text class="artist-tag" x="423">DJ K</text><text class="artist-tag" x="493">DJ K</text>
        </g>
        <g class="artist-tag-row" transform="translate(0 62)">
          <text class="artist-tag" x="27">DJ K</text><text class="artist-tag" x="93">DJ K</text><text class="artist-tag" x="159">DJ K</text><text class="artist-tag" x="225">DJ K</text><text class="artist-tag" x="291">DJ K</text><text class="artist-tag" x="357">DJ K</text><text class="artist-tag" x="423">DJ K</text><text class="artist-tag" x="493">DJ K</text>
        </g>
        <g class="artist-tag-row" transform="translate(0 472)">
          <text class="artist-tag" x="27">DJ K</text><text class="artist-tag" x="93">DJ K</text><text class="artist-tag" x="159">DJ K</text><text class="artist-tag" x="225">DJ K</text><text class="artist-tag" x="291">DJ K</text><text class="artist-tag" x="357">DJ K</text><text class="artist-tag" x="423">DJ K</text><text class="artist-tag" x="493">DJ K</text>
        </g>
        <g class="artist-tag-row" transform="translate(0 515)">
          <text class="artist-tag" x="27">DJ K</text><text class="artist-tag" x="93">DJ K</text><text class="artist-tag" x="159">DJ K</text><text class="artist-tag" x="225">DJ K</text><text class="artist-tag" x="291">DJ K</text><text class="artist-tag" x="357">DJ K</text><text class="artist-tag" x="423">DJ K</text><text class="artist-tag" x="493">DJ K</text>
        </g>
      </g>

      <g class="song-title-block">
        <text class="song-title" x="12" y="168" font-size="75" textLength="500" lengthAdjust="spacingAndGlyphs">TURN THE</text>
        <text class="song-title" x="12" y="279" font-size="117" textLength="500" lengthAdjust="spacingAndGlyphs">LIGHTS</text>
        <text class="song-title" x="12" y="416" font-size="153" textLength="500" lengthAdjust="spacingAndGlyphs">LOW</text>
      </g>
    </svg>
  </main>
</body>
</html>
```